Threadlane: fashion design product software needs your help

Fashion design product software company requests your assistance in designing a complete stationary package around our new logo design. Our software assists fashion designers and apparel houses with efficient communication and streamlined production between each other and manufacturers throughout the entire project design life cycle.

The look should reflect clean, simple and modern design. Not too "techie." Must use the provided logo and colors (or variations on the chosen colors, i.e. percentages as needed).

Reference website: www.threadlane-example.com

Buzzwords: manufacturing, production, apparel design/ers, streamlined process, effective communication, business, production software.

Please try to tone down or make the colors more subtle with more simple design style, layout. No sewing  theme. Thank you.

Target Market(s)

fashion designers and apparel houses that use software to manage and track production process life cycle.

Industry/Entity Type

Communication

Requirements
Must have
• Use of the logo and colors-or variations of colors (attached)
Nice to have
• Playfulness but corporate: with a sense of practicality, economical, streamlined production. Embossing considered.
Should not have
• Please keep in mind economics both financially and economically. Save trees and money! We believe in tactile paper but not "fashion-y" or sparkly, over-the-top colors, effects or production.

```html
<!DOCTYPE html>
<html lang="en">
<head>
<meta charset="utf-8">
<title>Threadlane Technologies Corp. – Business Card</title>
<link href="https://fonts.googleapis.com/css2?family=PT+Sans:wght@400;700&display=swap" rel="stylesheet">
<style>
  :root {
    --card-bg: #dde6ea;
    --accent-blue: #29b5e8;
    --accent-brown: #6b3420;
    --text-grey: #5b5b5b;
    --mark-faint: #d3dde2;
  }
  html, body {
    margin: 0;
    padding: 0;
    overflow: hidden;
    background: var(--card-bg);
  }
  .card {
    position: relative;
    width: 1200px;
    height: 695px;
    background: var(--card-bg);
    font-family: "PT Sans", Tahoma, sans-serif;
    overflow: hidden;
  }
  .card__frames {
    position: absolute;
    inset: 0;
  }
  .brand-mark {
    position: absolute;
    left: 80px;
    top: 243px;
    display: flex;
    align-items: center;
    gap: 18px;
  }
  .brand-mark__dot {
    width: 70px;
    height: 70px;
    border-radius: 50%;
    background: var(--mark-faint);
  }
  .brand-mark__name {
    font-size: 96px;
    font-weight: 700;
    color: var(--mark-faint);
    line-height: 1;
  }
  .company-name {
    position: absolute;
    right: 102px;
    top: 126px;
    margin: 0;
    font-size: 46px;
    font-weight: 400;
    color: var(--accent-blue);
    line-height: 1;
  }
  .contact {
    position: absolute;
    right: 119px;
    text-align: right;
    font-size: 33px;
    line-height: 45px;
    color: var(--text-grey);
    margin: 0;
  }
  .contact--address { top: 234px; }
  .contact--reach { top: 370px; }
  .website {
    position: absolute;
    left: 0;
    right: 0;
    top: 552px;
    text-align: center;
    font-size: 50px;
    letter-spacing: 1px;
    color: var(--accent-brown);
    line-height: 1;
    margin: 0;
    padding-right: 4px;
  }
</style>
</head>
<body>
  <main class="card">
    <svg class="card__frames" width="1200" height="695" viewBox="0 0 1200 695" aria-hidden="true">
      <polygon points="54,52 1134,110 1102,618 49,605" fill="none" stroke="var(--accent-blue)" stroke-width="4" stroke-dasharray="11 6"/>
      <polygon points="57,136 1105,47 1153,595 75,646" fill="none" stroke="var(--accent-brown)" stroke-width="4" stroke-dasharray="11 6"/>
    </svg>

    <div class="brand-mark" aria-hidden="true">
      <span class="brand-mark__name">threadlane</span>
      <span class="brand-mark__dot"></span>
    </div>

    <h1 class="company-name">Threadlane Technologies Corp.</h1>

    <p class="contact contact--address">214 Loomis Street<br>Riverton, NY 10990</p>
    <p class="contact contact--reach">Tel 555-014-2290<br>contact@threadlane-example.com</p>

    <p class="website">www.threadlane-example.com</p>
  </main>
</body>
</html>
```